Kelvane Electric short form flyer brochure

need a new brochure short form flyer to give to customers to highlight our capabilities,
we are merging 3 companies into one,
Kelvane Electric, Kelvane Forgeline, Kelvane Specialised portable buildings,
want to show case electrical Sheetmetal and building capabilities all on one bi fold out brochure, total 8 sided folded into A4,
pages as follows,
kelvane logo,
company profile,
electrical capabilities
electrical photos
Sheetmetal capabilities
sheet metal products
transportable buildings capabilities
range of other products.

will provide photos, most information will be on the web page,
www.kelvaneelectric.example.au

design needs to be fresh modern
any suggestions and tips will be welcomed

Target Market(s)

Utilities, power and water sectors, manufacturing

Requirements
Must have
• modern fresh design, bi fold into A4, total 8 sides design
Nice to have
• hints and tips to make it better, ask for information and photos if required

```html
<!DOCTYPE html>
<html lang="en">
<head>
<meta charset="utf-8">
<title>Kelvane Electric – Infrastructure Spread</title>
<link rel="stylesheet" href="https://fonts.googleapis.com/css2?family=Anton&family=Open+Sans:wght@400;600;700&family=Roboto:wght@700;900&display=swap">
<style>
  :root{
    --navy:#0f2a78;
    --blue:#1a3fa6;
    --blue-deep:#0a1f5e;
    --red:#ec1c2e;
    --white:#ffffff;
    --ink:#1d1d1d;
    --badge:#d9dde6;
  }
  *{box-sizing:border-box;margin:0;padding:0}
  html,body{width:1200px;height:899px;overflow:hidden;background:#e9e9e9}
  body{font-family:"Open Sans",Arial,sans-serif;color:var(--white)}
  h1,h2{font-weight:400}
  .spread{position:relative;width:1200px;height:899px;display:flex}
  .page{position:relative;width:600px;height:899px;overflow:hidden}

  /* left page */
  .page--left{background:var(--white)}
  .infra{position:absolute;left:0;top:0;width:600px;height:396px;
    background:linear-gradient(180deg,#173c9f 0%,#1a44ad 55%,#2753b8 78%,#1b3f9a 100%);padding:0 27px 0 31px}
  .infra__photo{position:absolute;left:0;right:0;bottom:0;height:140px;
    background:linear-gradient(180deg,rgba(26,63,166,0) 0%,rgba(120,150,210,.35) 60%,rgba(60,95,175,.5) 100%)}
  .infra__title{position:relative;font-family:"Anton",Impact,sans-serif;font-weight:400;color:var(--red);font-size:36px;
    text-align:center;letter-spacing:.5px;margin-top:40px;line-height:1.2;padding-left:20px}
  .section-head{position:relative;font-family:"Anton",Impact,sans-serif;font-weight:400;font-size:16px;letter-spacing:.3px;line-height:1.2}
  .infra .section-head{color:var(--red);margin-top:16px}
  .infra .section-head:first-of-type{margin-top:18px}
  .body-copy{position:relative;font-size:13.6px;line-height:1.38;text-align:justify;margin-top:5px}

  .factory{position:absolute;left:0;top:396px;width:600px;height:157px;background:var(--red);padding:16px 27px 0 31px}
  .factory .section-head{color:var(--white)}

  .contact{position:absolute;left:0;top:553px;width:600px;height:346px;background:var(--white);color:var(--ink)}
  .contact__map{position:absolute;left:35px;top:28px;width:210px;height:150px;border:2px solid #2b4fae;
    background:linear-gradient(135deg,#eef0e6 0%,#e3e8d6 40%,#cfe0c2 62%,#bcd7e6 78%,#e9ecea 100%)}
  .contact__details{position:absolute;left:280px;top:34px;font-size:15px;line-height:1.42}
  .contact__details p + p{margin-top:18px}
  .partners{position:absolute;left:33px;width:540px;display:flex;justify-content:space-between;align-items:center}
  .partners--top{top:222px}
  .partners--bottom{top:284px;width:540px}
  .partner-badge{display:block;height:22px;border-radius:4px;background:var(--badge)}

  /* right page */
  .page--right{background:var(--blue-deep)}
  .hero-photo{position:absolute;left:0;top:0;width:600px;height:605px;
    background:
      radial-gradient(ellipse 45% 30% at 70% 55%,rgba(240,200,40,.75),rgba(240,200,40,0) 70%),
      radial-gradient(ellipse 35% 25% at 85% 85%,rgba(245,210,60,.7),rgba(245,210,60,0) 70%),
      linear-gradient(120deg,#0d3a8c 0%,#1d63c7 30%,#3d8de0 50%,#1d4fa8 70%,#0b2a6e 100%)}
  .brand-corner{position:absolute;right:0;top:0;width:600px;height:300px}
  .brand-mark{position:absolute;left:400px;top:106px;display:flex;align-items:center;gap:8px;
    font-family:"Anton",Impact,sans-serif;font-weight:400;font-size:38px;color:var(--navy);line-height:1}
  .brand-mark__dot{width:16px;height:16px;border-radius:50%;background:var(--red)}
  .tagline-band{position:absolute;left:0;top:605px;width:600px;height:88px;background:var(--red);
    font-family:"Anton",Impact,sans-serif;font-weight:400;font-size:50px;text-align:center;line-height:88px;letter-spacing:.5px}
  .summary{position:absolute;left:0;top:693px;width:600px;height:140px;
    background:linear-gradient(180deg,#1c3f9f,#163590);padding:28px 50px 0 55px;font-size:15px;line-height:1.4}
  .summary blockquote{position:relative;padding-left:18px}
  .summary__quote{font-family:"Anton",Impact,sans-serif;font-size:28px;line-height:0}
  .summary__open{position:absolute;left:-6px;top:14px}
  .summary__close{vertical-align:-12px;margin-left:4px}
  .web-band{position:absolute;left:0;top:833px;width:600px;height:42px;background:var(--red);
    font-family:"Roboto",Arial,sans-serif;font-weight:900;font-size:24px;letter-spacing:2.5px;text-align:center;line-height:42px}
  .foot{position:absolute;left:0;top:875px;width:600px;height:24px;background:#163590}
</style>
</head>
<body>
<main class="spread">

  <section class="page page--left">
    <div class="infra">
      <div class="infra__photo" role="img" aria-label="Faint photograph of switchboard cabinets in the factory"></div>
      <h1 class="infra__title">INFRASTRUCTURE</h1>
      <h2 class="section-head">INTEGRATED ERP SYSTEM</h2>
      <p class="body-copy">Kelvane has a fully implemented and robust ERP system which handles the entire project, this allows us to provide accurate quoting, scheduling, and forecasting. We can also help manage reporting and costing for our clients.</p>
      <h2 class="section-head">DOCUMENT MANAGEMENT</h2>
      <p class="body-copy">Our cloud based system allows for a central depositary of documents for our projects, this system is hosted through Corvanet and Nimbrasoft and provides an easy interface for our clients and internal parties document control and sharing.</p>
    </div>

    <div class="factory">
      <h2 class="section-head">NEW FACTORY</h2>
      <p class="body-copy">In June, Kelvane moved to our new location which will house our three main businesses under one roof. The new factory will be located in Harlow Park and is adjacent to the Westlink freeway for ease of access and transportation. With over 7000 square meters of floor space we will be well placed to become leaders in Australia delivering complete solutions.</p>
    </div>

    <div class="contact">
      <div class="contact__map" role="img" aria-label="Street map marking the new factory location"></div>
      <div class="contact__details">
        <p>48 Brennock Drive<br>Harlow Park, VIC 3999, Australia</p>
        <p>+61 (0)3 5550 4500<br>+61 (0)3 5550 8785<br>info@kelvaneelectric.example.au</p>
      </div>
      <div class="partners partners--top" aria-label="Client and partner badges">
        <span class="partner-badge" style="width:56px"></span>
        <span class="partner-badge" style="width:52px"></span>
        <span class="partner-badge" style="width:70px"></span>
        <span class="partner-badge" style="width:56px;border-radius:50%"></span>
        <span class="partner-badge" style="width:40px"></span>
        <span class="partner-badge" style="width:36px"></span>
        <span class="partner-badge" style="width:48px"></span>
      </div>
      <div class="partners partners--bottom">
        <span class="partner-badge" style="width:64px"></span>
        <span class="partner-badge" style="width:44px"></span>
        <span class="partner-badge" style="width:38px"></span>
        <span class="partner-badge" style="width:22px;border-radius:50%"></span>
        <span class="partner-badge" style="width:60px"></span>
        <span class="partner-badge" style="width:58px"></span>
        <span class="partner-badge" style="width:56px"></span>
      </div>
    </div>
  </section>

  <section class="page page--right">
    <div class="hero-photo" role="img" aria-label="Close-up photograph of blue fibre optic connectors with yellow patch cables"></div>
    <svg class="brand-corner" viewBox="0 0 600 300" aria-hidden="true">
      <polygon points="296,0 600,0 600,306 370,226" fill="#0f2a78"/>
      <polygon points="308,0 600,0 600,296 382,218" fill="#ec1c2e"/>
      <polygon points="322,0 600,0 600,284 392,210" fill="#ffffff"/>
    </svg>
    <div class="brand-mark"><span class="brand-mark__dot"></span>Kelvane</div>

    <div class="tagline-band">TOTAL MCC SOLUTIONS</div>

    <div class="summary">
      <blockquote>
        <span class="summary__quote summary__open">&ldquo;</span>
        <p>Kelvane Group offers total solutions in the areas of electrical, sheet metal, portable building manufacturing, engineering, design, maintenance, and repairs site works.<span class="summary__quote summary__close">&rdquo;</span></p>
      </blockquote>
    </div>

    <div class="web-band">www.kelvaneelectric.example.au</div>
    <div class="foot"></div>
  </section>

</main>
</body>
</html>
```